K.T cleaning services

Want to attract different crowds for industrial, initial, commercial cleaning and window and carpet cleaning to be put on as well. A nice simple design where the K.T to be the logo maybe in a shape. And our slogan, K.T time K.T place K.T clean.

Target Market(s)

Constructions companies, office buildings, apartments, house owners,

Industry/Entity Type

Industrial

Contact Information for Business Card

Manager Gordon Tesslow 0437 851062

Logo Text

K.T Cleaning Services

Logo styles of interest
Emblem Logo
Requirements
Must have
• Email: k.tcleaning@mailnest-example.com

Slogan: K.T Time K.T Place K.T Clean

Family business equals quality
Nice to have
• I would to see ( K.T) inside a badge, and cleaning services underneath. Simple but eye catching please...

```html
<!DOCTYPE html>
<html lang="en">
<head>
<meta charset="utf-8">
<title>K.T Cleaning Services – Business Card</title>
<link rel="stylesheet" href="https://fonts.googleapis.com/css2?family=Arimo:wght@400;700&display=swap">
<style>
  :root {
    --paper: #ffffff;
    --ink: #414141;
    --brand: #4b97d5;
    --panel-top: #7dbaeb;
    --panel-bottom: #4b97d5;
    --panel-text: #ffffff;
  }
  html, body {
    margin: 0;
    padding: 0;
    overflow: hidden;
    background: var(--paper);
  }
  .card {
    position: relative;
    width: 1200px;
    height: 694px;
    background: var(--paper);
    overflow: hidden;
    font-family: "Arimo", Arial, sans-serif;
  }
  .slogan-line {
    position: absolute;
    display: flex;
    align-items: baseline;
    gap: 22px;
    white-space: nowrap;
    line-height: 1;
    font-weight: 700;
  }
  .brand-name {
    color: var(--brand);
    font-size: 96px;
    letter-spacing: -2px;
  }
  .slogan-word {
    color: var(--ink);
    font-size: 112px;
    letter-spacing: -3px;
  }
  .line-time  { left: 80px;  top: 104px; }
  .line-place { left: 128px; top: 310px; }
  .line-clean { left: 158px; top: 511px; }

  .contact-panel {
    position: absolute;
    left: 700px;
    top: 0;
    width: 500px;
    height: 694px;
    background: linear-gradient(180deg, var(--panel-top), var(--panel-bottom));
    color: var(--panel-text);
    text-align: center;
  }
  .services {
    position: absolute;
    left: 0;
    right: 0;
    top: 126px;
    margin: 0;
    font-size: 34px;
    font-weight: 400;
    line-height: 45px;
  }
  .manager-name {
    position: absolute;
    left: 0;
    right: 0;
    top: 452px;
    margin: 0;
    font-size: 44px;
    font-weight: 400;
    line-height: 1;
  }
  .manager-phone {
    position: absolute;
    left: 0;
    right: 0;
    top: 505px;
    margin: 0;
    font-size: 59px;
    font-weight: 700;
    line-height: 1;
  }
  .manager-email {
    position: absolute;
    left: 0;
    right: 0;
    top: 590px;
    margin: 0;
    font-size: 24px;
    font-weight: 400;
    line-height: 1;
  }
</style>
</head>
<body>
  <div class="card">
    <div class="slogan">
      <div class="slogan-line line-time">
        <span class="brand-name">K.T</span>
        <span class="slogan-word">Time.</span>
      </div>
      <div class="slogan-line line-place">
        <span class="brand-name">K.T</span>
        <span class="slogan-word">Place.</span>
      </div>
      <div class="slogan-line line-clean">
        <span class="brand-name">K.T</span>
        <span class="slogan-word">Clean.</span>
      </div>
    </div>

    <div class="contact-panel">
      <p class="services">Commercial &amp; domestic<br>cleaning services</p>
      <p class="manager-name">Gordon Tesslow</p>
      <p class="manager-phone">0437 851062</p>
      <p class="manager-email">k.tcleaning@mailnest-example.com</p>
    </div>
  </div>
</body>
</html>
```